Bright Path Academy - Personal Development business 2.0 needs a social post format design.

https://www.brightpathacademy-example.com

Our focus with Bright Path Academy is on developing people through knowledge and skills to improve their everyday lives.
We love simplicity, Quince design and less is more.

We are crazy about personal growth, science, design, the latest gadgets and people.

We need 4 formats for our social media posts.
1. Blogs -to pronounce a blog post
2. Workshop /training - to pronounce our workshops/trainings (both online and offline)
3. Podcast - called "Kijk eens verder". To pronounce a guest we've spoken. The host is called Berend.
4. Facts - to pronounce short facts about personal development. Invites people to read more.
The formats should include: high quality pictogram (better than the uploaded picto's), 1 of the 3 logo's in the design.
It's important that we can edit the design in Lumora Draw / Lumora Pixel to adjust the text in the format.

Attached you find four of our current designs, which are a poor example of how the designs should look like. These are just to show you how much lines of text (more or less) will be in the designs. So please do not make a design that looks like these ;) You have carte blanche.

Our customers are mostly women (80%). We focus on both business and casual customers.

Target Market(s)

80% woman, 20% men. We focus on both business and casual customers.

Requirements
Must have
• Less is more. Quince Design alike. Simplicity.
Aimed at the women target audience.
Designs must be edible for adjusting the text in the format.
Nice to have
• Unique concept.
The design should "breathe".
Each design can have a different color, so customers identify the specific post with specific information. For example, blog is red, workshop post black, etc.

```html
<!DOCTYPE html>
<html lang="nl">
<head>
<meta charset="utf-8">
<title>Bright Path Academy – Social Post Formats</title>
<link rel="stylesheet" href="https://fonts.googleapis.com/css2?family=Roboto+Condensed:wght@300;400;700&family=Fredoka:wght@600&display=swap">
<style>
  :root {
    --page-bg: #ffffff;
    --title-grey: #a8a8a8;
    --ink: #222222;
    --white: #ffffff;
    --frame-line: rgba(255, 255, 255, 0.28);
    --podcast-light: #63b2e4;
    --podcast-dark: #2d72b6;
    --podcast-accent: #2b8ad6;
    --podcast-navy: #123a78;
    --facts-light: #a03f90;
    --facts-dark: #4e2a80;
    --facts-accent: #7a2a86;
    --facts-pink: #a0288a;
    --training-light: #b0cb38;
    --training-dark: #5eab44;
    --training-accent: #57a83e;
    --blog-red: #cc3040;
    --blog-orange: #e0792e;
    --blog-yellow: #e9ae33;
    --blog-accent: #e58a2b;
    --blog-title: #d2342e;
  }
  * { box-sizing: border-box; margin: 0; padding: 0; }
  html, body { width: 960px; height: 1200px; overflow: hidden; background: var(--page-bg); }
  body { position: relative; font-family: "Roboto Condensed", sans-serif; }

  .sheet-title {
    position: absolute; top: 118px; left: 0; width: 960px; text-align: center;
    font-weight: 300; font-size: 44px; letter-spacing: 2px; color: var(--title-grey);
  }

  .post { position: absolute; width: 418px; height: 418px; overflow: hidden; }
  .post--podcast  { left: 43px;  top: 229px;
    background: radial-gradient(circle at 25% 80%, rgba(255,255,255,0.10), transparent 55%),
                linear-gradient(160deg, var(--podcast-light), var(--podcast-dark)); }
  .post--facts    { left: 500px; top: 229px;
    background: radial-gradient(circle at 20% 60%, rgba(40,15,80,0.25), transparent 55%),
                linear-gradient(160deg, var(--facts-light), var(--facts-dark)); }
  .post--training { left: 43px;  top: 666px;
    background: radial-gradient(circle at 80% 20%, rgba(255,255,255,0.12), transparent 55%),
                linear-gradient(160deg, var(--training-light), var(--training-dark)); }
  .post--blog     { left: 500px; top: 666px;
    background: radial-gradient(circle at 50% 55%, rgba(200,40,60,0.30), transparent 60%),
                linear-gradient(60deg, var(--blog-red) 20%, var(--blog-orange) 60%, var(--blog-yellow)); }

  .post__frame {
    position: absolute; left: 48px; top: 36px; width: 322px; height: 322px;
    border: 4px solid var(--frame-line); border-radius: 32px;
  }

  .post__card {
    position: absolute; left: 73px; top: 61px; width: 273px; height: 273px;
    background: var(--white); border-radius: 24px;
  }

  .post__brand {
    position: absolute; left: 0; width: 418px; top: 368px;
    display: flex; align-items: center; justify-content: center; gap: 8px;
    font-family: "Roboto Condensed", sans-serif; font-weight: 700; font-size: 28px;
    color: var(--white); line-height: 1;
  }
  .post__brand::before {
    content: ""; width: 14px; height: 14px; border-radius: 50%; background: var(--white);
  }

  .badge { position: absolute; left: 188px; top: 23px; width: 72px; height: 72px; border-radius: 50%;
           display: flex; align-items: center; justify-content: center; }
  .badge svg { width: 40px; height: 40px; }

  .label { position: absolute; font-family: "Fredoka", sans-serif; font-weight: 600; line-height: 1; }

  /* podcast */
  .guest-ring { position: absolute; left: 13px; top: 14px; width: 144px; height: 144px; }
  .guest-photo { position: absolute; left: 23px; top: 24px; width: 124px; height: 124px; border-radius: 50%;
                 background: radial-gradient(circle at 50% 40%, #d9b49a, #8a6a55 70%, #2a2a2a); }
  .post--podcast .badge { background: var(--podcast-accent); }
  .post--podcast .label { right: 14px; top: 96px; font-size: 21px; color: var(--podcast-accent); }
  .show-name { position: absolute; left: 0; width: 273px; top: 180px; text-align: center; font-size: 19px; color: var(--ink); }
  .guest-name { position: absolute; left: 0; width: 273px; top: 205px; text-align: center; font-size: 31px; font-weight: 700; color: var(--podcast-navy); }

  /* facts */
  .post--facts .badge { background: var(--facts-accent); }
  .post--facts .label { right: 102px; top: 44px; font-size: 36px; color: var(--facts-accent); }
  .fact-text { position: absolute; left: 0; width: 264px; top: 120px; text-align: center; font-size: 22px;
               font-weight: 700; line-height: 25px; color: var(--ink); }
  .fact-tag { position: absolute; left: 0; width: 264px; top: 218px; text-align: center; font-size: 19px; color: var(--facts-pink); }

  /* training */
  .post--training .badge { background: var(--training-accent); }
  .post--training .label { right: 104px; top: 38px; font-size: 27px; line-height: 25px; text-align: right; color: var(--training-accent); }
  .topic-title { position: absolute; left: 0; width: 273px; top: 156px; text-align: center; font-size: 32px; font-weight: 700; color: var(--ink); }
  .topic-date { position: absolute; left: 0; width: 273px; top: 194px; text-align: center; font-size: 19px; color: var(--training-accent); }

  /* blog */
  .post--blog .badge { background: var(--blog-accent); }
  .post--blog .label { right: 102px; top: 44px; font-size: 36px; color: var(--blog-accent); }
  .blog-title { position: absolute; left: 38px; top: 122px; font-size: 30px; font-weight: 700; color: var(--blog-title); }
  .blog-text { position: absolute; left: 38px; top: 158px; font-size: 20px; line-height: 25.5px; color: var(--ink); }
</style>
</head>
<body>
  <h1 class="sheet-title">DRAFT DESIGN</h1>

  <section class="post post--podcast">
    <div class="post__frame"></div>
    <div class="post__card">
      <svg class="guest-ring" viewBox="0 0 144 144" fill="none" stroke="#2b7fd0" stroke-width="4">
        <circle cx="72" cy="72" r="68"/>
      </svg>
      <div class="guest-photo" role="img" aria-label="Portretfoto van de podcastgast"></div>
      <div class="badge">
        <svg viewBox="0 0 40 40" fill="none" stroke="#ffffff" stroke-width="3" stroke-linecap="round">
          <rect x="14" y="5" width="12" height="20" rx="6" fill="#ffffff"/>
          <path d="M9 19a11 11 0 0 0 22 0"/>
          <path d="M20 30v5M14 35h12"/>
        </svg>
      </div>
      <span class="label">PODCAST</span>
      <p class="show-name">Kijk eens verder</p>
      <p class="guest-name">Joris van Dalen</p>
    </div>
    <p class="post__brand">Bright Path Academy</p>
  </section>

  <section class="post post--facts">
    <div class="post__frame"></div>
    <div class="post__card">
      <span class="label">FACTS</span>
      <div class="badge">
        <svg viewBox="0 0 40 40" fill="none" stroke="#ffffff" stroke-width="2.5" stroke-linecap="round" stroke-linejoin="round">
          <path d="M20 5c9 0 15 6 15 13s-6 13-15 13c-2 0-3 0-5-1l-7 4 2-7c-3-2-5-5-5-9C5 11 11 5 20 5z"/>
          <path d="M12 16h3l4-4v12l-4-4h-3z" fill="#ffffff"/>
          <path d="M23 14a5 5 0 0 1 0 8M26 11a9 9 0 0 1 0 14"/>
        </svg>
      </div>
      <p class="fact-text">The night vision of<br>tigers is 6 times better<br>than humans.</p>
      <p class="fact-tag">#DidYouKnow</p>
    </div>
    <p class="post__brand">Bright Path Academy</p>
  </section>

  <section class="post post--training">
    <div class="post__frame"></div>
    <div class="post__card">
      <span class="label">ONLINE<br>TRAINING</span>
      <div class="badge">
        <svg viewBox="0 0 40 40" fill="none" stroke="#ffffff" stroke-width="2.5" stroke-linecap="round" stroke-linejoin="round">
          <rect x="5" y="6" width="30" height="20" rx="2"/>
          <circle cx="13" cy="15" r="3" fill="#ffffff"/>
          <path d="M8 26v-3a5 5 0 0 1 10 0M18 20l8-6"/>
          <path d="M6 34h28"/>
        </svg>
      </div>
      <p class="topic-title">TOPIC Title Here</p>
      <p class="topic-date">January 25th</p>
    </div>
    <p class="post__brand">Bright Path Academy</p>
  </section>

  <section class="post post--blog">
    <div class="post__frame"></div>
    <div class="post__card">
      <span class="label">BLOG</span>
      <div class="badge">
        <svg viewBox="0 0 40 40" fill="none" stroke="#ffffff" stroke-width="2.5" stroke-linecap="round" stroke-linejoin="round">
          <path d="M27 6l7 7-17 17-9 2 2-9z"/>
          <path d="M23 10l7 7"/>
          <path d="M6 35h28"/>
        </svg>
      </div>
      <p class="blog-title">3 TIPS</p>
      <p class="blog-text">Lorem ipsum goede<br>voornemens die je<br>volhoudt</p>
    </div>
    <p class="post__brand">Bright Path Academy</p>
  </section>
</body>
</html>
```